Veterinary Business cards

Redesign Business Card

Information needed on Card:
Hours: Mon-Fri: 4pm -10PM; Sat- Sun- 10 AM- 5PM
Help@bayfernvet.com
www.bayfernvet.com
555-718-2946
4173 SE 19th Ave. okc, ok 73958
*No appointment necessary*

Optional:
Our tag line is "We're here when you need us" - If it fits on the cards.

```html
<!DOCTYPE html>
<html lang="en">
<head>
<meta charset="utf-8">
<title>Bayfern Vet Urgent Care – Business Card</title>
<link href="https://fonts.googleapis.com/css2?family=Poppins:wght@400;500&family=Satisfy&display=swap" rel="stylesheet">
<style>
  :root {
    --navy: #1b3d66;
    --orange: #e2922a;
    --orange-text: #e07f22;
    --white: #ffffff;
    --backdrop: #e6e6e8;
  }
  * { box-sizing: border-box; margin: 0; padding: 0; }
  html, body { width: 1200px; height: 900px; overflow: hidden; }
  body {
    background: var(--backdrop);
    font-family: "Poppins", Arial, sans-serif;
    display: flex;
    flex-direction: column;
    align-items: center;
    justify-content: center;
    gap: 40px;
  }
  .card {
    width: 700px;
    height: 400px;
    border-radius: 18px;
    position: relative;
    overflow: hidden;
  }

  /* Front */
  .card-front { background: var(--white); }
  .accent-circle {
    position: absolute;
    width: 420px; height: 420px;
    border-radius: 50%;
    background: var(--orange);
    right: -40px; top: -190px;
  }
  .brand {
    position: absolute;
    left: 44px; top: 70px;
  }
  .brand-name {
    color: var(--navy);
    font-weight: 500;
    font-size: 38px;
    line-height: 1.1;
    letter-spacing: 1px;
    text-transform: uppercase;
  }
  .brand-name .sub { display: block; font-size: 22px; letter-spacing: 4px; }
  .tagline {
    font-family: "Satisfy", cursive;
    color: var(--orange-text);
    font-size: 26px;
    margin-top: 10px;
  }
  .divider {
    position: absolute;
    left: 44px; right: 30px; top: 238px;
    height: 1.5px;
    background: var(--navy);
  }
  .contacts {
    position: absolute;
    left: 44px; top: 256px;
    list-style: none;
    color: var(--navy);
    font-size: 15px;
    line-height: 27px;
  }
  .contacts li, .hours-head { display: flex; align-items: center; gap: 10px; }
  .icon {
    width: 20px; height: 20px;
    border-radius: 50%;
    background: var(--orange);
    display: inline-flex; align-items: center; justify-content: center;
    flex-shrink: 0;
  }
  .icon svg { width: 12px; height: 12px; }
  .hours {
    position: absolute;
    left: 400px; top: 256px;
    color: var(--navy);
    font-size: 15px;
    line-height: 24px;
  }
  .hours .label { color: var(--orange-text); font-weight: 500; }
  .hours .indent { padding-left: 30px; }
  .hours .note { color: var(--orange-text); padding-left: 30px; }
  .band {
    position: absolute;
    left: 0; right: 0; bottom: 0;
    height: 40px;
    background: var(--navy);
    color: var(--white);
    font-size: 15px;
    display: flex; align-items: center; justify-content: center;
    letter-spacing: 0.5px;
  }

  /* Back */
  .card-back {
    background: var(--navy);
    display: flex; align-items: center; justify-content: center;
  }
  .back-name {
    color: var(--white);
    font-weight: 500;
    font-size: 46px;
    letter-spacing: 2px;
    text-transform: uppercase;
    text-align: center;
    line-height: 1.15;
  }
  .back-name .sub { display: block; font-size: 26px; letter-spacing: 6px; }
</style>
</head>
<body>

<section class="card card-front">
  <div class="accent-circle"></div>

  <div class="brand">
    <p class="brand-name">Bayfern Vet <span class="sub">Urgent Care</span></p>
    <p class="tagline">We're here when you need us</p>
  </div>

  <div class="divider"></div>

  <ul class="contacts">
    <li>
      <span class="icon"><svg viewBox="0 0 12 12"><path d="M2.5 1.5l2 .2.8 2.3-1.2.9a6 6 0 0 0 3 3l.9-1.2 2.3.8.2 2c-5 .8-9-3.2-8-8z" fill="#fff"/></svg></span>
      555-718-2946
    </li>
    <li>
      <span class="icon"><svg viewBox="0 0 12 12"><rect x="1.5" y="3" width="9" height="6.5" fill="none" stroke="#fff" stroke-width="1.2"/><path d="M1.5 3l4.5 3.6L10.5 3" fill="none" stroke="#fff" stroke-width="1.2"/></svg></span>
      Help@bayfernvet.com
    </li>
    <li>
      <span class="icon"><svg viewBox="0 0 12 12"><path d="M6 11s3.6-4 3.6-6.4A3.6 3.6 0 0 0 2.4 4.6C2.4 7 6 11 6 11z" fill="#fff"/><circle cx="6" cy="4.6" r="1.3" fill="#e2922a"/></svg></span>
      4173 SE 19th Ave. okc, ok 73958
    </li>
  </ul>

  <div class="hours">
    <p class="hours-head">
      <span class="icon"><svg viewBox="0 0 12 12"><circle cx="6" cy="6" r="4.3" fill="none" stroke="#fff" stroke-width="1.2"/><path d="M6 3.5V6h2" fill="none" stroke="#fff" stroke-width="1.2"/></svg></span>
      <span><span class="label">Hours:</span> Mon-Fri: 4pm -10PM</span>
    </p>
    <p class="indent">Sat- Sun- 10 AM- 5PM</p>
    <p class="note">No appointment necessary</p>
  </div>

  <div class="band">www.bayfernvet.com</div>
</section>

<section class="card card-back">
  <p class="back-name">Bayfern Vet <span class="sub">Urgent Care</span></p>
</section>

</body>
</html>
```